Webdesign für einen gemeinnützigen Verein
Zielgruppe
Merovalien e. V. ist ein gemeinnütziger Verein der sich auf die Fahne geschrieben hat sich für Inklusive und Vielfalt einzusetzen. Wir unterstützen Menschen mit Behinderung beim selbstbestimmten Leben und helfen auch bei Anträgen etc. Des weiteren helfen wir Firmen, Vereinen und stonstigen Organisationen Ihre Inhalte und Auftritte barrierefrei zu gestallten. Wir Testen Apps und Websites und geben hier Feedback.
Aufgabenstellung
Wir möchten ein WordPress Theme das responsiv und persistent ist. Wir möchten die Inhalte später mit WordPress Einpflege und die Seite managen.
Unser Corporate Design steht bereits und beinhaltet die Pride Farben und sollte somit in einem hellen und dunklen Design umgesetzt werden. Wir möchten hier 2 Varianten vom Homepage Design (Darkmode)
Poppins ist unsere Schriftart für Textinhalte
Google Fonds möchten wir nicht nutzen
Passende Social Media Icons

```html
<!DOCTYPE html>
<html lang="de">
<head>
<meta charset="utf-8">
<title>Merovalien e. V. – Homepage hell und dunkel</title>
<link rel="stylesheet" href="https://fonts.googleapis.com/css2?family=Poppins:wght@300;400;500;600;700&display=swap">
<style>
:root{
  --stage-grey:#dcdcdc;
  --stage-navy:#131a3a;
  --stage-white:#ffffff;
  --rainbow:linear-gradient(90deg,#e4312b 0%,#f08a24 20%,#f5d023 40%,#3aa74a 60%,#2f6fd6 80%,#7a2fb8 100%);
}
*{box-sizing:border-box;margin:0;padding:0}
html,body{width:1200px;height:3556px;overflow:hidden}
body{position:relative;font-family:"Poppins",sans-serif;background:var(--stage-white)}

.theme-light{
  --bg:#ffffff;--text:#2a2a2a;--accent:#4b176f;--nav-bg:#e9e9ea;--nav-text:#333333;
  --btn-bg:#4b176f;--btn-text:#ffffff;--quote:#d5c6e2;--deco:#f4f4f6;--deco-shadow:0 10px 24px rgba(0,0,0,.12);
  --icon:#4b176f;--brand:#4b176f;--toggle-bg:#ffffff;--toggle-knob:#4b176f;--arrow:#b9b9c4;
}
.theme-dark{
  --bg:linear-gradient(100deg,#3d1262 0%,#2b1652 55%,#151b3b 100%);--text:#ffffff;--accent:#ffffff;--nav-bg:#141a3a;--nav-text:#ffffff;
  --btn-bg:#ffffff;--btn-text:#4b176f;--quote:#5c2d84;--deco:#52197c;--deco-shadow:none;
  --icon:#ffffff;--brand:#ffffff;--toggle-bg:#4b176f;--toggle-knob:#ffffff;--arrow:#ffffff;
}

.stage{position:absolute;left:0;width:1200px}
.stage--grey{background:var(--stage-grey)}
.stage--navy{background:var(--stage-navy)}
.stage--white{background:var(--stage-white)}

.splash{position:absolute;background:var(--bg);overflow:hidden}
.splash__brand{position:absolute;left:0;right:0;text-align:center;font-weight:600;color:var(--brand);font-size:18px;letter-spacing:.5px}
.splash__bar{position:absolute;left:50%;height:3px;border-radius:2px;background:var(--rainbow);transform:translateX(-50%)}

.site{position:absolute;background:var(--bg);overflow:hidden;color:var(--text);transform-origin:top left}
.nav{position:absolute;left:0;top:0;right:0;background:var(--nav-bg);color:var(--nav-text)}
.brand{position:absolute;display:flex;align-items:center;gap:6px;font-weight:400;color:var(--nav-text)}
.brand__dot{width:12px;height:12px;border-radius:50%;background:var(--rainbow)}
.menu{position:absolute;font-size:9px}
.menu span{position:absolute;white-space:nowrap;top:0}
.menu .menu__home{background:var(--rainbow);color:#fff;border-radius:8px;padding:0 8px;line-height:13px}
.toggle{position:absolute;width:40px;height:20px;border-radius:10px;background:var(--toggle-bg);box-shadow:0 1px 4px rgba(0,0,0,.15)}
.toggle::before{content:"";position:absolute;left:5px;top:4px;width:12px;height:12px;border-radius:50%;background:var(--toggle-knob)}
.toggle::after{content:"";position:absolute;right:7px;top:6px;width:7px;height:7px;border-radius:50%;background:var(--nav-text)}
.burger{position:absolute;width:20px;height:18px;border-radius:5px;background:var(--rainbow)}
.burger i{position:absolute;left:5px;right:5px;height:2px;background:#fff;border-radius:1px}

.socials{position:absolute;display:flex}
.socials span{width:11px;height:11px;border-radius:50%;border:2px solid var(--icon);background:var(--icon)}
.theme-dark .socials span{background:transparent}

.deco{position:absolute;border-radius:40%;background:var(--deco);box-shadow:var(--deco-shadow)}

.hero-text{position:absolute;white-space:nowrap}
.hero-text p{line-height:1.6}
.hero-text .title{font-weight:600;color:var(--accent);letter-spacing:1px}
.hero-text .title::after{content:"";display:inline-block;width:1px;height:1em;background:var(--text);vertical-align:-2px;margin-left:2px}
.hero-text b{font-weight:600;color:var(--accent)}
.btn{position:absolute;background:var(--btn-bg);color:var(--btn-text);font-weight:600;border-radius:6px;text-align:center;letter-spacing:.3px;box-shadow:0 2px 5px rgba(0,0,0,.2)}
.quote-mark{position:absolute;font-weight:700;color:var(--quote);line-height:1}
.quote{position:absolute;text-align:center}
.arrow{position:absolute;width:11px;height:11px;border-left:1.5px solid var(--arrow);border-bottom:1.5px solid var(--arrow)}
.arrow--prev{transform:rotate(45deg)}
.arrow--next{transform:rotate(-135deg)}

/* desktop page 820 x 460 */
.site--desktop{width:820px;height:460px}
.site--desktop .nav{height:58px}
.site--desktop .brand{left:50px;top:19px;font-size:13px}
.site--desktop .brand__dot{width:18px;height:18px}
.site--desktop .menu{left:0;top:23px;width:100%}
.site--desktop .toggle{left:730px;top:19px}
.site--desktop .socials{left:642px;top:81px;gap:16px}
.site--desktop .deco{left:512px;top:105px;width:262px;height:228px}
.site--desktop .hero-text{left:110px;top:152px;font-size:19.5px}
.site--desktop .btn{left:112px;top:298px;width:90px;height:24px;font-size:8px;line-height:24px}
.site--desktop .quote-mark--open{left:108px;top:348px;font-size:70px}
.site--desktop .quote-mark--close{left:655px;top:398px;font-size:70px}
.site--desktop .quote{left:153px;top:385px;width:520px;font-size:14px;text-align:left}
.site--desktop .arrow--prev{left:54px;top:225px}
.site--desktop .arrow--next{left:760px;top:225px}

/* mobile page 258 x 460 */
.site--mobile{width:258px;height:460px}
.site--mobile .nav{height:42px}
.site--mobile .brand{left:14px;top:13px;font-size:10.5px}
.site--mobile .brand__dot{width:15px;height:15px}
.site--mobile .burger{left:222px;top:12px}
.site--mobile .socials{left:62px;top:88px;gap:19px}
.site--mobile .deco{left:24px;top:150px;width:190px;height:150px;opacity:.9}
.site--mobile .hero-text{left:0;right:0;top:130px;font-size:15.5px;text-align:center}
.site--mobile .hero-text p{line-height:1.7}
.site--mobile .btn{left:88px;top:312px;width:82px;height:22px;font-size:7px;line-height:22px}
.site--mobile .quote-mark--open{left:28px;top:337px;font-size:34px}
.site--mobile .quote-mark--close{left:205px;top:385px;font-size:34px}
.site--mobile .quote{left:20px;right:20px;top:357px;font-size:9px;line-height:1.8}
.site--mobile .arrow--prev{left:98px;top:432px}
.site--mobile .arrow--next{left:156px;top:432px}
</style>
</head>
<body>

<!-- Hell: Geräteansicht -->
<section class="stage stage--grey" style="top:0;height:780px">
  <div class="splash theme-light" style="left:55px;top:262px;width:242px;height:428px">
    <div class="splash__brand" style="top:168px">merovalien</div>
    <div class="splash__bar" style="top:227px;width:132px"></div>
  </div>

  <div class="site site--desktop theme-light" style="left:225px;top:124px;transform:scale(.905)">
    <header class="nav">
      <div class="brand"><span class="brand__dot"></span>MEROVALIEN</div>
      <nav class="menu"><span class="menu__home" style="left:295px;top:-1px">Home</span><span style="left:363px">Verein</span><span style="left:420px">Projekte</span><span style="left:489px">Team</span><span style="left:541px">Blog</span><span style="left:585px">Wir im Netz</span><span style="left:659px">Kontakt</span></nav>
      <span class="toggle"></span>
    </header>
    <div class="socials"><span></span><span></span><span></span><span></span><span></span></div>
    <div class="deco" role="img" aria-label="Großes Vereinszeichen als Dekoration"></div>
    <div class="hero-text"><p class="title">MEROVA</p><p>Verein zur Stärkung der</p><p><b>Teilhabe</b> und <b>Vielfalt</b></p><p>für ein eigenständiges Leben e. V.</p></div>
    <span class="btn">MEHR ERFAHREN</span>
    <span class="quote-mark quote-mark--open">“</span>
    <p class="quote">Verständigung baut Brücken zur Teilhabe : Merovalien öffnet Wege</p>
    <span class="quote-mark quote-mark--close">”</span>
  </div>

  <div class="site site--mobile theme-light" style="left:913px;top:262px;transform:scale(.93)">
    <header class="nav"><div class="brand"><span class="brand__dot"></span>MEROVALIEN</div><span class="burger"><i style="top:5px"></i><i style="top:8px"></i><i style="top:11px"></i></span></header>
    <div class="socials"><span></span><span></span><span></span><span></span><span></span></div>
    <div class="deco" role="img" aria-label="Vereinszeichen als Hintergrunddekoration"></div>
    <div class="hero-text"><p class="title">MEROVALIE</p><p>Verein zur Stärkung</p><p>der <b>Teilhabe</b></p><p>und <b>Vielfalt</b> für ein</p><p>eigenständiges</p><p>Leben e. V.</p></div>
    <span class="btn">MEHR ERFAHREN</span>
    <span class="quote-mark quote-mark--open">“</span>
    <p class="quote">Verständigung baut Brücken zur Teilhabe :<br>Merovalien öffnet Wege</p>
    <span class="quote-mark quote-mark--close">”</span>
    <span class="arrow arrow--prev"></span><span class="arrow arrow--next"></span>
  </div>
</section>

<!-- Hell: Einzelansichten -->
<section class="stage stage--navy" style="top:780px;height:999px">
  <div class="splash theme-light" style="left:36px;top:38px;width:258px;height:461px">
    <div class="splash__brand" style="top:200px">merovalien</div>
    <div class="splash__bar" style="top:281px;width:142px"></div>
  </div>
  <div class="splash theme-light" style="left:344px;top:38px;width:820px;height:461px">
    <div class="splash__brand" style="top:200px">merovalien</div>
    <div class="splash__bar" style="top:281px;width:142px"></div>
  </div>

  <div class="site site--mobile theme-light" style="left:36px;top:499px">
    <header class="nav"><div class="brand"><span class="brand__dot"></span>MEROVALIEN</div><span class="burger"><i style="top:5px"></i><i style="top:8px"></i><i style="top:11px"></i></span></header>
    <div class="socials"><span></span><span></span><span></span><span></span><span></span></div>
    <div class="deco" role="img" aria-label="Vereinszeichen als Hintergrunddekoration"></div>
    <div class="hero-text"><p class="title">MEROVALIE</p><p>Verein zur Stärkung</p><p>der <b>Teilhabe</b></p><p>und <b>Vielfalt</b> für ein</p><p>eigenständiges</p><p>Leben e. V.</p></div>
    <span class="btn">MEHR ERFAHREN</span>
    <span class="quote-mark quote-mark--open">“</span>
    <p class="quote">Verständigung baut Brücken zur Teilhabe :<br>Merovalien öffnet Wege</p>
    <span class="quote-mark quote-mark--close">”</span>
    <span class="arrow arrow--prev"></span><span class="arrow arrow--next"></span>
  </div>

  <div class="site site--desktop theme-light" style="left:344px;top:499px">
    <header class="nav">
      <div class="brand"><span class="brand__dot"></span>MEROVALIEN</div>
      <nav class="menu"><span class="menu__home" style="left:295px;top:-1px">Home</span><span style="left:363px">Verein</span><span style="left:420px">Projekte</span><span style="left:489px">Team</span><span style="left:541px">Blog</span><span style="left:585px">Wir im Netz</span><span style="left:659px">Kontakt</span></nav>
      <span class="toggle"></span>
    </header>
    <div class="socials"><span></span><span></span><span></span><span></span><span></span></div>
    <div class="deco" role="img" aria-label="Großes Vereinszeichen als Dekoration"></div>
    <div class="hero-text"><p class="title">MEROVA</p><p>Verein zur Stärkung der</p><p><b>Teilhabe</b> und <b>Vielfalt</b></p><p>für ein eigenständiges Leben e. V.</p></div>
    <span class="btn">MEHR ERFAHREN</span>
    <span class="quote-mark quote-mark--open">“</span>
    <p class="quote">Verständigung baut Brücken zur Teilhabe : Merovalien öffnet Wege</p>
    <span class="quote-mark quote-mark--close">”</span>
    <span class="arrow arrow--prev"></span><span class="arrow arrow--next"></span>
  </div>
</section>

<!-- Dunkel: Geräteansicht -->
<section class="stage stage--grey" style="top:1779px;height:779px">
  <div class="splash theme-dark" style="left:55px;top:262px;width:242px;height:428px">
    <div class="splash__brand" style="top:168px">merovalien</div>
    <div class="splash__bar" style="top:227px;width:132px"></div>
  </div>

  <div class="site site--desktop theme-dark" style="left:225px;top:124px;transform:scale(.905)">
    <header class="nav">
      <div class="brand"><span class="brand__dot"></span>MEROVALIEN</div>
      <nav class="menu"><span class="menu__home" style="left:295px;top:-1px">Home</span><span style="left:363px">Verein</span><span style="left:420px">Projekte</span><span style="left:489px">Team</span><span style="left:541px">Blog</span><span style="left:585px">Wir im Netz</span><span style="left:659px">Kontakt</span></nav>
      <span class="toggle"></span>
    </header>
    <div class="socials"><span></span><span></span><span></span><span></span><span></span></div>
    <div class="deco" role="img" aria-label="Großes Vereinszeichen als Dekoration"></div>
    <div class="hero-text"><p class="title">Merovalie</p><p>Verein zur Stärkung der</p><p><b>Teilhabe</b> und <b>Vielfalt</b></p><p>für ein eigenständiges Leben e. V.</p></div>
    <span class="btn">MEHR ERFAHREN</span>
    <span class="quote-mark quote-mark--open">“</span>
    <p class="quote">Verständigung baut Brücken zur Teilhabe : Merovalien öffnet Wege</p>
    <span class="quote-mark quote-mark--close">”</span>
  </div>

  <div class="site site--mobile theme-dark" style="left:913px;top:262px;transform:scale(.93)">
    <header class="nav"><div class="brand"><span class="brand__dot"></span>MEROVALIEN</div><span class="burger"><i style="top:5px"></i><i style="top:8px"></i><i style="top:11px"></i></span></header>
    <div class="socials"><span></span><span></span><span></span><span></span><span></span></div>
    <div class="deco" role="img" aria-label="Vereinszeichen als Hintergrunddekoration"></div>
    <div class="hero-text"><p class="title">Merovalie</p><p>Verein zur Stärkung</p><p>der <b>Teilhabe</b></p><p>und <b>Vielfalt</b> für ein</p><p>eigenständiges</p><p>Leben e. V.</p></div>
    <span class="btn">MEHR ERFAHREN</span>
    <span class="quote-mark quote-mark--open">“</span>
    <p class="quote">Verständigung baut Brücken zur Teilhabe :<br>Merovalien öffnet Wege</p>
    <span class="quote-mark quote-mark--close">”</span>
    <span class="arrow arrow--prev"></span><span class="arrow arrow--next"></span>
  </div>
</section>

<!-- Dunkel: Einzelansichten -->
<section class="stage stage--white" style="top:2558px;height:998px">
  <div class="splash theme-dark" style="left:36px;top:38px;width:258px;height:461px">
    <div class="splash__brand" style="top:200px">merovalien</div>
    <div class="splash__bar" style="top:281px;width:142px"></div>
  </div>
  <div class="splash theme-dark" style="left:344px;top:38px;width:820px;height:461px">
    <div class="splash__brand" style="top:200px">merovalien</div>
    <div class="splash__bar" style="top:281px;width:142px"></div>
  </div>

  <div class="site site--mobile theme-dark" style="left:36px;top:499px">
    <header class="nav"><div class="brand"><span class="brand__dot"></span>MEROVALIEN</div><span class="burger"><i style="top:5px"></i><i style="top:8px"></i><i style="top:11px"></i></span></header>
    <div class="socials"><span></span><span></span><span></span><span></span><span></span></div>
    <div class="deco" role="img" aria-label="Vereinszeichen als Hintergrunddekoration"></div>
    <div class="hero-text"><p class="title">Merovalie</p><p>Verein zur Stärkung</p><p>der <b>Teilhabe</b></p><p>und <b>Vielfalt</b> für ein</p><p>eigenständiges</p><p>Leben e. V.</p></div>
    <span class="btn">MEHR ERFAHREN</span>
    <span class="quote-mark quote-mark--open">“</span>
    <p class="quote">Verständigung baut Brücken zur Teilhabe :<br>Merovalien öffnet Wege</p>
    <span class="quote-mark quote-mark--close">”</span>
    <span class="arrow arrow--prev"></span><span class="arrow arrow--next"></span>
  </div>

  <div class="site site--desktop theme-dark" style="left:344px;top:499px">
    <header class="nav">
      <div class="brand"><span class="brand__dot"></span>MEROVALIEN</div>
      <nav class="menu"><span class="menu__home" style="left:295px;top:-1px">Home</span><span style="left:363px">Verein</span><span style="left:420px">Projekte</span><span style="left:489px">Team</span><span style="left:541px">Blog</span><span style="left:585px">Wir im Netz</span><span style="left:659px">Kontakt</span></nav>
      <span class="toggle"></span>
    </header>
    <div class="socials"><span></span><span></span><span></span><span></span><span></span></div>
    <div class="deco" role="img" aria-label="Großes Vereinszeichen als Dekoration"></div>
    <div class="hero-text"><p class="title">Merovalie</p><p>Verein zur Stärkung der</p><p><b>Teilhabe</b> und <b>Vielfalt</b></p><p>für ein eigenständiges Leben e. V.</p></div>
    <span class="btn">MEHR ERFAHREN</span>
    <span class="quote-mark quote-mark--open">“</span>
    <p class="quote">Verständigung baut Brücken zur Teilhabe : Merovalien öffnet Wege</p>
    <span class="quote-mark quote-mark--close">”</span>
    <span class="arrow arrow--prev"></span><span class="arrow arrow--next"></span>
  </div>
</section>

</body>
</html>
```